bluegum ridge coaching needs snazzy business card that serves a dual purpose

business card needed for a Bluegum Ridge Coaching company that takes people out on the road to teach them proficiency on their bike.
My business logo is attached. I have grey and aqua colours with my logo.
i really like bitumen/tarmac/ road in the design somehow but that is up to you.
I think navy blue will go well with my colours too. see how you go.

I want this card to look REALLY good.
the back of the card may be used for emergency contact details too
In case of Emergency I am:
Name:

Emergency Contact name
emergency contact Phone number:

• details that are essential are:
• logo
• Name: Helena FORD
• ABN: 53 291 804 667
• phone number: 0455 128 906
• chatterly logo
• * ride tuition & proficiency
• * skills practice
• * maintenance 101
• * bike fitting service
• * cater for all ages & abilities
• backpage:
• logo
• skills confidence enjoyment
• some space for writing
• nothing girly. The business will already naturally attract women, it needs to appeal to both genders

```html
<!DOCTYPE html>
<html lang="en">
<head>
<meta charset="utf-8">
<title>Bluegum Ridge Coaching – Business Card</title>
<link href="https://fonts.googleapis.com/css2?family=Montserrat:wght@400;500;700&display=swap" rel="stylesheet">
<style>
  :root {
    --backdrop: #1bae9b;
    --aqua-light: #5ec6b6;
    --aqua-mid: #4fb3a4;
    --aqua-deep: #3f9f91;
    --charcoal: #3a3d3f;
    --card-edge: #55585b;
    --white: #ffffff;
  }
  * { box-sizing: border-box; margin: 0; padding: 0; }
  html, body { width: 1200px; height: 800px; overflow: hidden; }
  body {
    background: var(--backdrop);
    font-family: "Montserrat", Arial, sans-serif;
    color: var(--charcoal);
    position: relative;
  }
  .card {
    position: absolute;
    top: 250px;
    width: 440px;
    height: 290px;
    background: var(--aqua-light);
    overflow: hidden;
    box-shadow: 0 6px 0 var(--card-edge), 0 14px 24px rgba(0,0,0,0.18);
  }
  .card--front { left: 138px; }
  .card--back { left: 622px; }

  .road-graphic {
    position: absolute;
    inset: 0;
    background:
      radial-gradient(ellipse 60% 40% at 30% 80%, rgba(63,159,145,0.55), transparent 70%),
      radial-gradient(ellipse 50% 35% at 75% 20%, rgba(63,159,145,0.45), transparent 70%),
      linear-gradient(160deg, var(--aqua-light), var(--aqua-mid));
  }

  /* Front */
  .contact {
    position: absolute;
    top: 22px;
    right: 28px;
    text-align: right;
    font-size: 12px;
    line-height: 17px;
  }
  .contact__name { font-weight: 700; font-size: 14px; margin-bottom: 2px; }
  .contact__phone svg { width: 10px; height: 10px; vertical-align: -1px; margin-right: 3px; }

  .logo-band {
    position: absolute;
    left: 0; right: 0;
    top: 97px;
    height: 104px;
    background: var(--white);
    display: flex;
    align-items: center;
    justify-content: center;
  }
  .brand-name {
    font-weight: 500;
    font-size: 27px;
    letter-spacing: 1px;
    color: var(--charcoal);
  }
  .tagline {
    position: absolute;
    top: 211px;
    left: 0; right: 0;
    text-align: center;
    font-size: 12px;
    letter-spacing: 2.4px;
    text-transform: uppercase;
  }
  .dot-icon {
    display: inline-block;
    width: 14px; height: 14px;
    vertical-align: -2px;
    margin: 0 8px;
  }
  .social {
    position: absolute;
    right: 26px;
    bottom: 18px;
    display: flex;
    align-items: center;
    gap: 6px;
    font-size: 12px;
    font-weight: 500;
  }
  .social__square { width: 20px; height: 20px; background: var(--charcoal); }

  /* Back */
  .header-band {
    position: absolute;
    left: 0; right: 0;
    top: 18px;
    height: 54px;
    background: var(--white);
    display: flex;
    align-items: center;
    justify-content: space-between;
    padding: 0 22px 0 36px;
  }
  .brand-name--small { font-size: 15px; letter-spacing: 0.5px; }
  .service-headline { font-size: 11px; font-weight: 700; text-transform: uppercase; align-self: flex-end; margin-bottom: 6px; }

  .services {
    position: absolute;
    top: 83px;
    left: 112px;
    list-style: none;
    font-size: 12px;
    letter-spacing: 1.6px;
    text-transform: uppercase;
  }
  .services li { height: 25px; display: flex; align-items: center; }
  .services .dot-icon { margin: 0 8px 0 0; }

  .emergency-form {
    position: absolute;
    left: 18px; right: 18px;
    top: 183px;
    height: 92px;
    background: var(--white);
    padding: 6px 14px 0 22px;
    font-size: 11px;
  }
  .emergency-form__row {
    display: flex;
    height: 20px;
    align-items: flex-end;
    white-space: nowrap;
  }
  .emergency-form__line {
    flex: 1;
    border-bottom: 1.5px dotted var(--charcoal);
    margin: 0 0 3px 6px;
  }
</style>
</head>
<body>

<section class="card card--front">
  <div class="road-graphic" role="img" aria-label="Winding road graphic in aqua tones"></div>
  <div class="contact">
    <p class="contact__name">Helena FORD</p>
    <p>ABN: 53 291 804 667</p>
    <p class="contact__phone"><svg viewBox="0 0 10 10"><path d="M2 1 L4 1 L4.5 3 L3.5 4 Q4.5 5.8 6 6.5 L7 5.5 L9 6 L9 8 Q5 9 1 3 Z" fill="currentColor"/></svg>: 0455 128 906</p>
  </div>
  <div class="logo-band">
    <span class="brand-name">Bluegum Ridge Coaching</span>
  </div>
  <p class="tagline">
    Skills<svg class="dot-icon" viewBox="0 0 14 14"><circle cx="7" cy="7" r="6" fill="none" stroke="currentColor" stroke-width="1.6"/><circle cx="7" cy="7" r="1.6" fill="currentColor"/></svg>Confidence<svg class="dot-icon" viewBox="0 0 14 14"><circle cx="7" cy="7" r="6" fill="none" stroke="currentColor" stroke-width="1.6"/><circle cx="7" cy="7" r="1.6" fill="currentColor"/></svg>Enjoyment
  </p>
  <div class="social">
    <span class="social__square"></span>
    <span>chatterly</span>
  </div>
</section>

<section class="card card--back">
  <div class="road-graphic" role="img" aria-label="Winding road graphic in aqua tones"></div>
  <div class="header-band">
    <span class="brand-name brand-name--small">Bluegum Ridge Coaching</span>
    <span class="service-headline">Ride tuition &amp; proficiency</span>
  </div>
  <ul class="services">
    <li><svg class="dot-icon" viewBox="0 0 14 14"><circle cx="7" cy="7" r="6" fill="none" stroke="currentColor" stroke-width="1.6"/><circle cx="7" cy="7" r="1.6" fill="currentColor"/></svg>Skills practice</li>
    <li><svg class="dot-icon" viewBox="0 0 14 14"><circle cx="7" cy="7" r="6" fill="none" stroke="currentColor" stroke-width="1.6"/><circle cx="7" cy="7" r="1.6" fill="currentColor"/></svg>Maintenance 101</li>
    <li><svg class="dot-icon" viewBox="0 0 14 14"><circle cx="7" cy="7" r="6" fill="none" stroke="currentColor" stroke-width="1.6"/><circle cx="7" cy="7" r="1.6" fill="currentColor"/></svg>Bike fitting service</li>
    <li><svg class="dot-icon" viewBox="0 0 14 14"><circle cx="7" cy="7" r="6" fill="none" stroke="currentColor" stroke-width="1.6"/><circle cx="7" cy="7" r="1.6" fill="currentColor"/></svg>Cater for all ages &amp; abilities</li>
  </ul>
  <div class="emergency-form">
    <div class="emergency-form__row">I am :<span class="emergency-form__line"></span></div>
    <div class="emergency-form__row">Name :<span class="emergency-form__line"></span></div>
    <div class="emergency-form__row">Emergency Contact Name :<span class="emergency-form__line"></span></div>
    <div class="emergency-form__row">Emergency Contact Phone Number :<span class="emergency-form__line"></span></div>
  </div>
</section>

</body>
</html>
```